Flyer-Design / Verodina
Zielgruppe
Licht zu verstehen und richtig einzusetzen ist ein wesentlicher Bestandteil, um die Wirkung von Architektur, Innenräumen und Landschaften zu unterstützen und zu steigern. Die harmonische Verschmelzung von moderner Architektur und akzentuiert eingesetztem Licht verleiht Innenräumen ihre eigene Note. Dieses Zusammenspiel erfordert über das Berechnen und die Leuchtenauswahl hinaus einen sehr sensiblen Umgang mit dem Medium Licht. Bei jeder Lichtplanung steht der Mensch mit seiner Wahrnehmung von Licht und Schatten im Mittelpunkt. Eine hochwertige Lichtplanung vom Fachmann verfolgt mit ihrem ganzheitlichen Ansatz daher den Anspruch Atmosphäre, Wohlbefinden und Orientierung zu schaffen und den beleuchteten Räumen Ausdruckskraft zu verleihen.
Aufgabenstellung
WIr möchten einen Flyer für unseren Laden der für den Kunden sehr ansprechend ist, im Bezug auf unserer Planungen und unseren Handel.
Wir möchten darauf eine Zusammenfassung unser Arbeit und unserer Portfolios sehen die dem Kunden sofort sagen was wir machen.

```html
<!DOCTYPE html>
<html lang="de">
<head>
<meta charset="utf-8">
<title>Verodina – Flyer</title>
<link href="https://fonts.googleapis.com/css2?family=Arimo:wght@400&family=Questrial&display=swap" rel="stylesheet">
<style>
:root{
  --anthracite:#313537;
  --yellow:#ffe500;
  --paper:#ffffff;
  --ink:#2b2b2b;
  --photo-dark-a:#45494c;
  --photo-dark-b:#232527;
  --photo-light-a:#e4e5e6;
  --photo-light-b:#9c9ea0;
}
*{margin:0;padding:0;box-sizing:border-box}
html,body{width:1200px;height:1200px;overflow:hidden;background:var(--paper)}
body{position:relative;font-family:"Arimo",Arial,sans-serif;color:var(--ink)}
.board-label{position:absolute;font-family:"Questrial",sans-serif;font-size:25px;color:#1d1d1d}
.panel{position:absolute;overflow:hidden;background:var(--anthracite);box-shadow:2px 3px 5px rgba(0,0,0,.35)}
.sun{position:absolute;border-radius:50%;background:var(--yellow)}
.brand{position:absolute;text-align:right}
.brand-name{font-size:27px;letter-spacing:5px;color:var(--paper);line-height:1;display:flex;align-items:center;justify-content:flex-end;gap:8px}
.brand-dot{width:9px;height:9px;border-radius:50%;background:var(--yellow);display:inline-block}
.brand-claim{font-size:7.5px;letter-spacing:1.3px;color:#9a9d9f;margin-top:10px;text-align:left;padding-left:86px;line-height:1.2}
.slogan{position:absolute;font-size:26px;line-height:1;white-space:nowrap}
.slogan .on-sun{color:var(--ink)}
.slogan .on-dark{color:var(--paper);margin-left:8px}
.contact{position:absolute;text-align:right;font-size:9.6px;line-height:11.6px;color:var(--ink)}
.leaflet{position:absolute;background:var(--paper);overflow:hidden}
.headline{font-size:15px;color:var(--yellow);position:absolute}
.copy{position:absolute;font-size:7.4px;line-height:9.6px;color:#333}
.copy p{margin-bottom:9.6px}
.claim{position:absolute;font-size:26px;line-height:31.5px;color:var(--ink)}
.grid-cell{position:absolute;overflow:hidden}
.cell-dark{background:var(--anthracite);display:flex;align-items:center;justify-content:center;text-align:center;color:var(--yellow);font-size:9.6px;line-height:11.6px;padding:0 8px}
.cell-white{background:var(--paper)}
.cell-white .copy{left:12px;right:12px;top:40px}
.photo-pendant{background:linear-gradient(160deg,var(--photo-dark-a),var(--photo-dark-b))}
.photo-chandelier{background:radial-gradient(circle at 50% 45%,#d8d8d8,#ffffff 70%)}
.photo-wall{background:radial-gradient(circle at 50% 40%,#d5d6d8,#8f9193 85%)}
.photo-ceiling{background:linear-gradient(180deg,var(--photo-light-a),var(--photo-light-b))}
</style>
</head>
<body>

<!-- Aussen -->
<section class="panel" style="left:28px;top:23px;width:678px;height:479px" aria-label="Außenseite">
  <div class="leaflet" style="left:12px;top:11px;width:214px;height:468px"></div>
  <div class="sun" style="left:0;top:314px;width:216px;height:216px;left:-2px"></div>
  <h2 class="headline" style="left:20px;top:24px">Headline Headline</h2>
  <div class="copy" style="left:19px;top:80px;width:198px">
    <p>Lorem ipsum dolor sit amet, consectetuer adipiscing elit. Aenean commodo ligula eget dolor. Aenean massa. Cum sociis natoque penatibus et magnis dis parturient montes, nascetur ridiculus mus. Donec quam felis, ultricies nec, pellentesque eu, pretium quis, sem.</p>
    <p>Nulla consequat massa quis enim. Donec pede justo, fringilla vel, aliquet nec, vulputate eget, arcu. In enim justo, rhoncus ut, imperdiet a, venenatis vitae, justo. Nullam dictum felis eu pede mollis pretium. Integer tincidunt. Cras dapibus. Vivamus elementum semper nisi.</p>
    <p>Aenean vulputate eleifend tellus. Aenean leo ligula, porttitor eu, consequat vitae, eleifend ac, enim. Aliquam lorem ante, dapibus in, viverra quis, feugiat a, tellus. Phasellus viverra nulla ut metus varius laoreet.</p>
    <p>Quisque rutrum. Aenean imperdiet.</p>
  </div>
  <p class="claim" style="left:20px;top:380px">bei uns finden<br>Sie die richtige<br>Leuchte</p>

  <div class="sun" style="left:277px;top:232px;width:350px;height:350px"></div>
  <div class="brand" style="left:440px;top:58px;width:222px">
    <div class="brand-name"><span class="brand-dot"></span>VERODINA</div>
    <div class="brand-claim">Lichtberatung +<br>Fachhandel</div>
  </div>
  <p class="slogan" style="left:470px;top:316px"><span class="on-sun">wir machen</span><span class="on-dark">licht</span></p>
  <address class="contact" style="right:237px;top:365px;font-style:normal">
    verodina<br>Lindenhofweg 12<br>91234 Sonnfeld<br>Tel: +49 9123-4567890<br>Email: info@verodina.de<br>www. verodina.de<br><br>Öffnungszeiten:<br>(Mo–Fr.) 8:00–17:00
  </address>
</section>
<p class="board-label" style="left:50px;top:510px">aussen</p>

<!-- Titel -->
<section class="panel" style="left:727px;top:23px;width:224px;height:479px" aria-label="Titel">
  <div class="sun" style="left:-177px;top:232px;width:350px;height:350px"></div>
  <div class="brand" style="left:-14px;top:58px;width:222px">
    <div class="brand-name"><span class="brand-dot"></span>VERODINA</div>
    <div class="brand-claim">Lichtberatung +<br>Fachhandel</div>
  </div>
  <p class="slogan" style="left:16px;top:316px"><span class="on-sun">wir machen</span><span class="on-dark">licht</span></p>
</section>
<p class="board-label" style="left:734px;top:510px">Titel</p>

<!-- Rückseite -->
<section class="panel" style="left:971px;top:23px;width:224px;height:479px" aria-label="Rückseite">
  <div class="sun" style="left:51px;top:232px;width:350px;height:350px"></div>
  <address class="contact" style="right:9px;top:365px;font-style:normal">
    verodina<br>Lindenhofweg 12<br>91234 Sonnfeld<br>Tel: +49 9123-4567890<br>Email: info@verodina.de<br>www. verodina.de<br><br>Öffnungszeiten:<br>(Mo–Fr.) 8:00–17:00
  </address>
</section>
<p class="board-label" style="left:976px;top:502px">Rückseite</p>

<!-- Innen -->
<section class="panel" style="left:40px;top:583px;width:677px;height:479px" aria-label="Innenseite">
  <div class="grid-cell photo-pendant" role="img" aria-label="Foto: schwarze Pendelleuchte über einem Tisch" style="left:0;top:0;width:112px;height:159px"></div>
  <div class="grid-cell cell-dark" style="left:112px;top:0;width:113px;height:159px">Lorem ipsum dolor sit amet, consectetuer adipiscing elit.</div>
  <div class="grid-cell photo-chandelier" role="img" aria-label="Foto: Kristall-Kronleuchter" style="left:225px;top:0;width:114px;height:159px"></div>
  <div class="grid-cell cell-dark" style="left:339px;top:0;width:112px;height:159px">Lorem ipsum dolor sit amet, consectetuer adipiscing elit.</div>
  <div class="grid-cell cell-white" style="left:451px;top:0;width:226px;height:159px">
    <div class="copy" style="top:37px">
      <p>Lorem ipsum dolor sit amet, consectetuer adipiscing elit. Aenean commodo ligula eget dolor. Aenean massa. Cum sociis natoque penatibus et magnis dis parturient montes, nascetur ridiculus mus. Donec quam felis, ultricies nec, pellentesque eu, pretium quis, sem.</p>
      <p>Nulla consequat massa quis enim. Donec pede justo, fringilla vel, aliquet nec, vulputate eget, arcu. In enim justo, rhoncus ut, imperdiet a, venenatis vitae, justo. Nullam dictum felis eu pede mollis pretium. Integer tincidunt. Cras dapibus. Vivamus elementum semper nisi.</p>
    </div>
  </div>

  <div class="grid-cell cell-white" style="left:0;top:159px;width:225px;height:161px">
    <div class="copy" style="top:35px">
      <p>Lorem ipsum dolor sit amet, consectetuer adipiscing elit. Aenean commodo ligula eget dolor. Aenean massa. Cum sociis natoque penatibus et magnis dis parturient montes, nascetur ridiculus mus. Donec quam felis, ultricies nec, pellentesque eu, pretium quis, sem.</p>
      <p>Nulla consequat massa quis enim. Donec pede justo, fringilla vel, aliquet nec, vulputate eget, arcu. In enim justo, rhoncus ut, imperdiet a, venenatis vitae, justo. Nullam dictum felis eu pede mollis pretium. Integer tincidunt. Cras dapibus. Vivamus elementum semper nisi.</p>
    </div>
  </div>
  <div class="grid-cell cell-dark" style="left:225px;top:159px;width:114px;height:161px">Lorem ipsum dolor sit amet, consectetuer adipiscing elit.</div>
  <div class="grid-cell photo-wall" role="img" aria-label="Foto: dunkle runde Wandleuchte mit Lichtschein" style="left:339px;top:159px;width:112px;height:161px"></div>
  <div class="grid-cell cell-dark" style="left:451px;top:159px;width:114px;height:161px">Lorem ipsum dolor sit amet, consectetuer adipiscing elit.</div>
  <div class="grid-cell photo-wall" role="img" aria-label="Foto: schwarze Wandleuchte mit goldenem Inneren" style="left:565px;top:159px;width:112px;height:161px"></div>

  <div class="grid-cell photo-ceiling" role="img" aria-label="Foto: weiße Deckenleuchte" style="left:0;top:320px;width:112px;height:159px"></div>
  <div class="grid-cell cell-dark" style="left:112px;top:320px;width:113px;height:159px">Lorem ipsum dolor sit amet, consectetuer adipiscing elit.</div>
  <div class="grid-cell cell-white" style="left:225px;top:320px;width:226px;height:159px">
    <div class="copy" style="top:28px">
      <p>Lorem ipsum dolor sit amet, consectetuer adipiscing elit. Aenean commodo ligula eget dolor. Aenean massa. Cum sociis natoque penatibus et magnis dis parturient montes, nascetur ridiculus mus. Donec quam felis, ultricies nec, pellentesque eu, pretium quis, sem.</p>
      <p>Nulla consequat massa quis enim. Donec pede justo, fringilla vel, aliquet nec, vulputate eget, arcu. In enim justo, rhoncus ut, imperdiet a, venenatis vitae, justo. Nullam dictum felis eu pede mollis pretium. Integer tincidunt. Cras dapibus. Vivamus elementum semper nisi.</p>
    </div>
  </div>
  <div class="grid-cell photo-ceiling" role="img" aria-label="Foto: weiße Deckenleuchte" style="left:451px;top:320px;width:114px;height:159px"></div>
  <div class="grid-cell cell-dark" style="left:565px;top:320px;width:112px;height:159px">Lorem ipsum dolor sit amet, consectetuer adipiscing elit.</div>
</section>
<p class="board-label" style="left:38px;top:1088px">innen</p>

<!-- 1x aufgeklappt -->
<section class="panel" style="left:747px;top:585px;width:439px;height:500px" aria-label="Einmal aufgeklappt">
  <div class="grid-cell photo-pendant" role="img" aria-label="Foto: schwarze Pendelleuchte über einem Tisch" style="left:0;top:0;width:110px;height:167px"></div>
  <div class="grid-cell cell-dark" style="left:110px;top:0;width:110px;height:167px">Lorem ipsum dolor sit amet, consectetuer adipiscing elit.</div>
  <div class="grid-cell cell-white" style="left:0;top:167px;width:220px;height:167px">
    <div class="copy" style="top:30px">
      <p>Lorem ipsum dolor sit amet, consectetuer adipiscing elit. Aenean commodo ligula eget dolor. Aenean massa. Cum sociis natoque penatibus et magnis dis parturient montes, nascetur ridiculus mus. Donec quam felis, ultricies nec, pellentesque eu, pretium quis, sem.</p>
      <p>Nulla consequat massa quis enim. Donec pede justo, fringilla vel, aliquet nec, vulputate eget, arcu. In enim justo, rhoncus ut, imperdiet a, venenatis vitae, justo. Nullam dictum felis eu pede mollis pretium. Integer tincidunt. Cras dapibus. Vivamus elementum semper nisi.</p>
    </div>
  </div>
  <div class="grid-cell photo-ceiling" role="img" aria-label="Foto: weiße Deckenleuchte" style="left:0;top:334px;width:110px;height:166px"></div>
  <div class="grid-cell cell-dark" style="left:110px;top:334px;width:110px;height:166px">Lorem ipsum dolor sit amet, consectetuer adipiscing elit.</div>

  <div class="leaflet" style="left:220px;top:10px;width:211px;height:490px">
    <div class="sun" style="left:-40px;top:334px;width:220px;height:220px"></div>
    <h2 class="headline" style="left:19px;top:24px">Headline Headline</h2>
    <div class="copy" style="left:18px;top:80px;width:188px">
      <p>Lorem ipsum dolor sit amet, consectetuer adipiscing elit. Aenean commodo ligula eget dolor. Aenean massa. Cum sociis natoque penatibus et magnis dis parturient montes, nascetur ridiculus mus. Donec quam felis, ultricies nec, pellentesque eu, pretium quis, sem.</p>
      <p>Nulla consequat massa quis enim. Donec pede justo, fringilla vel, aliquet nec, vulputate eget, arcu. In enim justo, rhoncus ut, imperdiet a, venenatis vitae, justo. Nullam dictum felis eu pede mollis pretium. Integer tincidunt. Cras dapibus. Vivamus elementum semper nisi.</p>
      <p>Aenean vulputate eleifend tellus. Aenean leo ligula, porttitor eu, consequat vitae, eleifend ac, enim. Aliquam lorem ante, dapibus in, viverra quis, feugiat a, tellus. Phasellus viverra nulla ut metus varius laoreet.</p>
      <p>Quisque rutrum. Aenean imperdiet.</p>
    </div>
    <p class="claim" style="left:18px;top:385px">bei uns finden<br>Sie die richtige<br>Leuchte</p>
  </div>
</section>
<p class="board-label" style="left:768px;top:1140px">1x aufgeklappt</p>

</body>
</html>
```